Launch of Kolvaro.com

Need a banner ad for the launch of a new website that covers Singapore, Australia and India. The website is www.kolvaro.example (the Singapore one is www.kolvaro.example.sg and the India one is www.kolvaro.example.in). Note that all three are english speaking countries and the ad need to be in english.

The value proposition are :

a. It has all job listings available in the country and many times larger the nearest competitor job listing.
b. You can find almost any job you want in the country, kinda of infinite choices for you.
c. It is the coolest and hippest jobs search site.
(Avoid green and orange as they are the competitors' colors)
Updates

Project Deadline Extended
Reason: Some of the designs have come in pretty good, but need some touch up. I have given the feedback and appreciate the need to time to change.

Project Deadline Extended
Reason: I realised that the tagline that I guided you looks and sounds awful. I am making some changes and will revert to you. Sorry.

Target Market(s)

Mass market

Requirements
Must have
• Be daring in the statement, be bold in trying out use of pictures or graphics that is controversial or suggestive, as long it is not porn.
Should not have
• Premium look, or appeal only to the professional .

```html
<!DOCTYPE html>
<html lang="en">
<head>
<meta charset="utf-8">
<title>Kolvaro.com – Launch Banner</title>
<link rel="stylesheet" href="https://fonts.googleapis.com/css2?family=Open+Sans:wght@400;600;700&display=swap">
<style>
  :root {
    --stage-grey: #8c8d8f;
    --sky-white: #f6fbfe;
    --sky-pale: #e3f3fa;
    --sky-cyan: #9fd9ec;
    --brand-blue: #2ba4dc;
    --tagline-grey: #5c6270;
    --band-yellow: #f4cf4a;
    --band-text: #6d6a62;
    --wood-light: #f1e6d2;
    --wood-mid: #e2cfae;
  }

  * { margin: 0; padding: 0; box-sizing: border-box; }

  html, body {
    width: 1200px;
    height: 900px;
    overflow: hidden;
    background: var(--stage-grey);
    font-family: "Open Sans", Arial, sans-serif;
  }

  .banner {
    position: absolute;
    left: 375px;
    top: 262px;
    width: 450px;
    height: 375px;
    overflow: hidden;
    background:
      radial-gradient(ellipse 55% 70% at 100% 40%, var(--sky-cyan) 0%, rgba(159,217,236,0) 70%),
      radial-gradient(ellipse 60% 50% at 15% 60%, #ffffff 0%, rgba(255,255,255,0) 80%),
      linear-gradient(160deg, var(--sky-white) 0%, var(--sky-pale) 100%);
  }

  .brand-name {
    position: absolute;
    left: 20px;
    top: 12px;
    font-size: 66px;
    font-weight: 400;
    letter-spacing: -1px;
    line-height: 1;
    color: var(--brand-blue);
  }

  .tagline {
    position: absolute;
    left: 22px;
    top: 100px;
    font-size: 27px;
    font-weight: 600;
    line-height: 34px;
    color: var(--tagline-grey);
    letter-spacing: -0.3px;
  }

  .letter-blocks {
    position: absolute;
    left: 120px;
    top: 162px;
    width: 325px;
    height: 164px;
    border-radius: 6px;
    background: linear-gradient(180deg, var(--wood-light) 0%, var(--wood-mid) 100%);
  }

  .country-band {
    position: absolute;
    left: 0;
    top: 327px;
    width: 330px;
    height: 39px;
    background: var(--band-yellow);
    display: flex;
    align-items: center;
    padding-left: 16px;
    font-size: 15px;
    font-weight: 700;
    letter-spacing: 1px;
    color: var(--band-text);
    white-space: nowrap;
  }

  .country-band .divider {
    margin: 0 10px;
    font-weight: 400;
  }
</style>
</head>
<body>
  <div class="banner">
    <div class="brand-name">Kolvaro</div>
    <p class="tagline">coolest and hippest<br>jobs search site</p>
    <div class="letter-blocks" role="img" aria-label="Wooden toy alphabet blocks showing the letters A, T, O and Z"></div>
    <div class="country-band">
      SINGAPORE<span class="divider">|</span>AUSTRALIA<span class="divider">|</span>INDIA
    </div>
  </div>
</body>
</html>
```